VelmoraHub

Hey

I am involved with crowd funding, please look at one of my current sites www.funsprell.com
Work is currently under way with a new site www.velmorahub.com .wehave the basics but I am not happy with what we have so far. I need to redesign the web site but keep the concept . The cartoon pitch will be kept , along with some of the other functions which we can help you with, unless you are able to build / design something better. I liked a lot of the designs submitted for a previous crowd funning design, far better than what I currently have. To be included on this site will be links to numerous crowd funding sites which I have registered but each site will be focused on a specific topic which will be disclosed once this site is active. I intend to build all these sites through this site. Along with these sites will be a logo design for each site so plenty of work going forward. I have a logo for velmorahub already but am open for improvements and suggestions but would like to keep a map or logo of Africa included in the design. To bear in mind this is a African focused buisness which aims to help communities, employment creation, poverty alleviation and help young entrepreneurs kickstarter their buisness . I already have a group logo , which was designed on this site ( look at tandel yards competition) , I would like this logo to be used on all the site so customers and investors link the group and concept togeather. Here is the link http://www.brievoshop.co.uk/project-progress.aspx?briefId=48213 . I have removed the tandelyard from the bottom of the logo and will just be using the figurines as the group logo on all web sites. There will be at least fifty related crowd fund projects linked to this site.
If any body has any questions or ideas please feel free to ask for anything you may need. Thanks to everybody who helps with this project. Warmly. Ravi

Hi everyone working on my design.

The contact details to use on the site are

27 Weltmore Close
Dunvale
Cape Town 
+263748395026
+447913462058

E mail enquiries@VelmoraHub.example

There are two logos, one is the velmorahub logo and the other is my group logo which I will attach to the pitch
Good luck and thank you to everybody who is working on this web design
Warmly

Ravi

```html
<!DOCTYPE html>
<html lang="en">
<head>
<meta charset="utf-8">
<title>VelmoraHub – Equity Crowdfunding</title>
<link rel="stylesheet" href="https://fonts.googleapis.com/css2?family=Ubuntu:wght@400;500;700&family=Arimo:wght@400;700&display=swap">
<style>
:root{
  --red:#d8311e;
  --red-dark:#b52414;
  --red-text:#c8251a;
  --ink:#333;
  --muted:#555;
  --green:#7aa226;
  --blue:#1a8fd0;
  --nav-dark:#3a2a28;
  --panel:#ececec;
  --footer:#4a4a4a;
  --footer-text:#e8e8e8;
}
*{margin:0;padding:0;box-sizing:border-box}
html,body{width:1007px;height:1200px;overflow:hidden;background:#fff}
body{position:relative;font-family:Arimo,Arial,sans-serif;color:var(--ink)}
.abs{position:absolute}

/* top nav */
.topnav{left:0;top:0;width:1007px;height:27px;background:linear-gradient(#e0412c,#c92a18)}
.topnav a{position:absolute;top:0;height:27px;line-height:27px;font-size:10.5px;color:#fff;text-decoration:none;font-family:Ubuntu,sans-serif;text-transform:uppercase}
.topnav .active{background:var(--nav-dark);padding:0 12px;left:86px;width:55px;text-align:center;font-weight:500}
.topnav .sep{position:absolute;top:4px;width:1px;height:19px;background:rgba(255,255,255,.3)}
.topnav .split{position:absolute;left:620px;top:0;width:387px;height:27px;background:linear-gradient(#cf3320,#b82413);clip-path:polygon(38px 0,100% 0,100% 100%,0 100%)}
.topnav .small{font-size:9.5px;font-weight:500}

/* header */
.header{left:0;top:27px;width:1007px;height:107px;background:linear-gradient(#fff,#f2f2f2)}
.brand{left:86px;top:60px;display:flex;align-items:center;gap:8px}
.brand .dot{width:30px;height:30px;border-radius:50%;background:var(--blue)}
.brand .name{font-family:Ubuntu,sans-serif;font-weight:700;font-size:22px;color:var(--blue)}
.login-title{left:566px;top:56px;font-family:Ubuntu,sans-serif;font-size:16px;color:#555}
.field{top:54px;width:99px;height:24px;border-radius:12px;background:#fff;border:1px solid #ddd;box-shadow:inset 0 1px 3px rgba(0,0,0,.12);font-size:8.5px;color:#777;padding:7px 12px}
.btn-login{left:871px;top:56px;width:52px;height:23px;border-radius:7px;background:linear-gradient(#e54b33,#c4270f);color:#fff;font-size:11px;font-family:Ubuntu,sans-serif;text-align:center;line-height:23px}
.register{left:790px;top:100px;font-size:9px;color:#666}
.register b{color:var(--red-text);font-style:italic;margin-left:4px}

/* hero */
.hero{left:0;top:134px;width:1007px;height:344px;background:linear-gradient(#c9421f 0%,#d2532a 55%,#8a2a12 80%,#1b0a05 100%)}
.photo{border-radius:50%;border:9px solid #f3f3f3;box-shadow:0 4px 14px rgba(0,0,0,.35)}
.photo.team{left:86px;top:179px;width:280px;height:280px;background:radial-gradient(circle at 50% 40%,#e9edf1,#a9b3bd)}
.photo.office{left:312px;top:140px;width:150px;height:150px;background:radial-gradient(circle,#e8e6e2,#b7b0a6)}
.photo.sketch{left:354px;top:228px;width:208px;height:208px;background:radial-gradient(circle at 60% 40%,#f6efe9,#c8b4a5)}

/* categories */
.cats{left:702px;top:122px;width:229px;height:352px;background:#f7f5f4;border-radius:6px 6px 14px 14px;box-shadow:0 2px 8px rgba(0,0,0,.3)}
.cats h2{position:absolute;left:10px;top:14px;font-family:Ubuntu,sans-serif;line-height:1}
.cats h2 .a{display:block;font-size:15px;color:var(--red-text);font-weight:700}
.cats h2 .b{display:block;font-size:23px;color:#3a3a3a;font-weight:700}
.cats ul{list-style:none;position:absolute;left:3px;top:63px;width:225px}
.cats li{height:36px;margin-bottom:4px;background:linear-gradient(#f2f2f2,#d9d9d9);font-family:Ubuntu,sans-serif;font-size:13px;color:#3a3a3a;line-height:36px;padding-left:15px;text-transform:uppercase}
.cats li.on{background:linear-gradient(#e54a32,#c92c16);color:#fff;position:relative}
.cats li.on::before{content:"";position:absolute;left:-16px;top:2px;width:32px;height:32px;border-radius:50%;background:#f7f5f4;box-shadow:inset -2px 0 3px rgba(0,0,0,.15)}
.cats li.on::after{content:"";position:absolute;left:-4px;top:11px;border:7px solid transparent;border-right-color:var(--red);border-left:0}

/* welcome */
.welcome{left:90px;top:494px;width:535px}
.welcome h1{font-family:Ubuntu,sans-serif;font-weight:400;font-size:18px;color:#555;padding:0 0 6px 35px;border-bottom:1px dotted #bbb;position:relative}
.welcome h1 strong{color:var(--red-text);font-weight:500}
.welcome h1 .mark{position:absolute;left:0;top:0;width:24px;height:24px;border-radius:50%;background:var(--blue)}
.lead{font-size:9.5px;font-weight:700;line-height:17px;margin-top:8px;color:#222}
.tag{font-size:9.5px;color:var(--red-text);margin-top:9px}
.points{list-style:none;margin-top:10px}
.points li{font-size:9.5px;color:#444;line-height:16.8px;padding-left:30px;position:relative}
.points li::before{content:"";position:absolute;left:18px;top:5px;border:3.5px solid transparent;border-left:5px solid #e8a21a;border-right:0}
.cta{left:90px;top:733px;font-size:10.5px;font-weight:700;color:#333}

/* video */
.vid-title{left:683px;top:500px;font-family:Ubuntu,sans-serif;font-size:17px;color:#555;padding-bottom:5px;border-bottom:1px dotted #bbb;width:197px}
.vid-title strong{color:var(--red-text);font-weight:500}
.vid{left:671px;top:532px;width:221px;height:188px;border-radius:14px;background:linear-gradient(#f1f1f1,#dcdcdc);box-shadow:0 6px 6px -4px rgba(0,0,0,.4)}
.vid .screen{position:absolute;left:10px;top:10px;width:201px;height:150px;border-radius:10px;background:linear-gradient(#b7b9b8,#8d908f)}
.vid .play{position:absolute;left:80px;top:50px;width:56px;height:56px;border-radius:50%;background:rgba(70,70,70,.55);border:3px solid rgba(255,255,255,.8)}
.vid .play::after{content:"";position:absolute;left:20px;top:14px;border:11px solid transparent;border-left:17px solid #fff;border-right:0}
.vid .cap{position:absolute;left:20px;top:167px;font-size:8.5px;color:#333}
.vid .cap i{display:inline-block;width:6px;height:6px;border-radius:50%;background:var(--red);margin-right:2px}

.rule{left:90px;top:776px;width:833px;border-top:1px dotted #bbb}

/* project cards */
.card{top:800px;width:200px;height:230px}
.card + .card{}
.card .vline{position:absolute;left:-8px;top:-8px;height:232px;border-left:1px dotted #bbb}
.card h3{font-family:Ubuntu,sans-serif;font-weight:400;font-size:15px;color:var(--red-text);margin-left:8px}
.card .pic{position:absolute;left:0;top:33px;width:196px;height:80px;border:4px solid #fff;box-shadow:0 0 0 1px #ddd,0 2px 3px rgba(0,0,0,.15)}
.card p{position:absolute;left:0;top:125px;width:190px;font-size:9.5px;line-height:15px;color:#444;letter-spacing:.6px;text-align:justify}
.card p b{color:#222}
.card .backers{position:absolute;left:0;top:196px;display:flex;align-items:center;gap:10px;font-family:Arial,sans-serif;font-size:22px;color:#444}
.card .funded{position:absolute;right:20px;top:196px;font-size:11.5px;line-height:19px;text-align:left}
.card .funded .f{color:var(--red-text)}
.card .funded .g{color:var(--green)}

/* footer */
.footer{left:0;top:1057px;width:1007px;height:143px;background:var(--footer);color:var(--footer-text)}
.foot-brand{left:92px;top:1110px;display:flex;align-items:center;gap:10px}
.foot-brand .dot{width:40px;height:40px;border-radius:50%;background:#8a8a8a}
.foot-brand .name{font-family:Ubuntu,sans-serif;font-size:25px;color:#9a9a9a}
.fsep{top:1067px;height:123px;border-left:1px dotted #888}
.foot-links{left:360px;top:1069px;width:335px;font-size:10px;text-align:center}
.follow{left:360px;top:1100px;width:315px;text-align:center;font-size:10px}
.social{left:444px;top:1120px;display:flex;gap:11px}
.social span{width:32px;height:32px;border-radius:50%;background:radial-gradient(circle at 40% 35%,#fff,#d6d6d6);box-shadow:0 1px 2px rgba(0,0,0,.4)}
.copy{left:360px;top:1175px;width:335px;text-align:center;font-size:10px}
.contact{right:95px;top:1063px;text-align:right;font-size:10px;line-height:15.2px}
.contact h4{font-family:Ubuntu,sans-serif;font-size:16px;color:#bdbdbd;font-weight:500;line-height:20px}
.contact b{font-size:11.5px;color:#fff}
</style>
</head>
<body>

<nav class="abs topnav">
  <span class="split"></span>
  <a class="active">Blog</a>
  <a style="left:159px">IPO'S</a>
  <span class="sep" style="left:212px"></span>
  <a style="left:235px">How it works</a>
  <span class="sep" style="left:332px"></span>
  <a style="left:352px">About</a>
  <span class="sep" style="left:408px"></span>
  <a style="left:430px">My account</a>
  <span class="sep" style="left:527px"></span>
  <a style="left:562px">My cart</a>
  <a class="small" style="left:656px">Join now</a>
  <span class="sep" style="left:715px"></span>
  <a class="small" style="left:726px">How it works ?</a>
  <span class="sep" style="left:812px"></span>
  <a class="small" style="left:825px">Browse companies</a>
</nav>

<header class="abs header"></header>
<div class="abs brand"><span class="dot"></span><span class="name">VelmoraHub</span></div>
<div class="abs login-title">Login Now</div>
<div class="abs field" style="left:654px">Username</div>
<div class="abs field" style="left:763px">Password</div>
<div class="abs btn-login">Login</div>
<div class="abs register">Register &nbsp;/ <b>Forgot Password</b></div>

<section class="abs hero" role="img" aria-label="Savanna sunset scene in red and orange with tree and animal silhouettes"></section>
<div class="abs photo office" role="img" aria-label="Photo of a business team in an office"></div>
<div class="abs photo team" role="img" aria-label="Photo of smiling business people"></div>
<div class="abs photo sketch" role="img" aria-label="Photo of a woman sketching a diagram"></div>

<aside class="abs cats">
  <h2><span class="a">BUSINESS</span><span class="b">CATEGORIES</span></h2>
  <ul>
    <li class="on">Comics</li>
    <li>Environment</li>
    <li>Fashion</li>
    <li>Film and Video</li>
    <li>Gaming</li>
    <li>Health and Fitness</li>
    <li>IT and Telecomunications</li>
  </ul>
</aside>

<section class="abs welcome">
  <h1><span class="mark"></span>Welcome to <strong>Africa’s leading crowdfunding</strong></h1>
  <p class="lead">Crowdfunding enables people to raise money for innovative new projects by getting like-minded individuals to pool their money to back the idea,</p>
  <p class="tag">Person or business. It’s a way to make things happen.</p>
  <ul class="points">
    <li>Lorem Ipsum is simply dummy text of the printing</li>
    <li>Lorem Ipsum has been the industry's standard dummy text</li>
    <li>when an unknown printer took a galley of type and</li>
    <li>It has survived not only five centuries, but also</li>
    <li>when an unknown printer took a galley of type and</li>
    <li>Relocation Comprehensive range of boxes and packing materials for sale</li>
    <li>when an unknown printer took a galley of type and</li>
  </ul>
</section>
<p class="abs cta">What are you waiting for? Call us NOW on 02 7315 2089. We will exceed your expectations.</p>

<h2 class="abs vid-title">What is <strong>Crowdfunding?</strong></h2>
<div class="abs vid">
  <div class="screen" role="img" aria-label="Cartoon pitch video still"></div>
  <div class="play"></div>
  <div class="cap"><i></i><i></i> Watch Latest Testimonial Video</div>
</div>

<div class="abs rule"></div>

<article class="abs card" style="left:90px">
  <h3>Ut Placerat nunc suscipit</h3>
  <div class="pic" role="img" aria-label="Photo of blue and white hydrangea flowers" style="background:linear-gradient(120deg,#2f5a22,#c9cfe8 55%,#2c4a1c)"></div>
  <p><b>Ut placerat nunc suscipit metus lacinia vel interdum tortor</b> eleifend. Aliquam erat volutpat. Ut consectetur auctor ornare.</p>
  <div class="backers"><svg width="28" height="28" viewBox="0 0 28 28"><circle cx="9" cy="8" r="4" fill="#b98a5a"/><circle cx="19" cy="8" r="4" fill="#b98a5a"/><path d="M2 22c0-6 14-6 14 0z" fill="#4a7a2a"/><path d="M12 22c0-6 14-6 14 0z" fill="#3a5a8a"/><circle cx="14" cy="14" r="4" fill="#c99a6a"/><path d="M6 28c0-7 16-7 16 0z" fill="#555"/></svg>0</div>
  <div class="funded"><div class="f">Funded $0</div><div class="g">Goal $1,000</div></div>
</article>

<article class="abs card" style="left:300px">
  <span class="vline"></span>
  <h3>Proin in ante et nulla</h3>
  <div class="pic" role="img" aria-label="Photo of penguins on ice" style="background:linear-gradient(#9fc7e4,#e6f0f7 60%,#bcd3e4)"></div>
  <p><b>Ut placerat nunc suscipit metus lacinia vel interdum tortor</b> eleifend. Aliquam erat volutpat. Ut consectetur auctor ornare.</p>
  <div class="backers"><svg width="28" height="28" viewBox="0 0 28 28"><circle cx="9" cy="8" r="4" fill="#b98a5a"/><circle cx="19" cy="8" r="4" fill="#b98a5a"/><path d="M2 22c0-6 14-6 14 0z" fill="#4a7a2a"/><path d="M12 22c0-6 14-6 14 0z" fill="#3a5a8a"/><circle cx="14" cy="14" r="4" fill="#c99a6a"/><path d="M6 28c0-7 16-7 16 0z" fill="#555"/></svg>0</div>
  <div class="funded"><div class="f">Funded $0</div><div class="g">Goal $1,000</div></div>
</article>

<article class="abs card" style="left:509px">
  <span class="vline"></span>
  <h3>Vestibulum sed nulla</h3>
  <div class="pic" role="img" aria-label="Photo of a purple allium flower" style="background:radial-gradient(circle at 55% 55%,#8b6ad8,#3c5fa8 50%,#1d5e8a)"></div>
  <p><b>Ut placerat nunc suscipit metus lacinia vel interdum tortor</b> eleifend. Aliquam erat volutpat. Ut consectetur auctor ornare.</p>
  <div class="backers"><svg width="28" height="28" viewBox="0 0 28 28"><circle cx="9" cy="8" r="4" fill="#b98a5a"/><circle cx="19" cy="8" r="4" fill="#b98a5a"/><path d="M2 22c0-6 14-6 14 0z" fill="#4a7a2a"/><path d="M12 22c0-6 14-6 14 0z" fill="#3a5a8a"/><circle cx="14" cy="14" r="4" fill="#c99a6a"/><path d="M6 28c0-7 16-7 16 0z" fill="#555"/></svg>0</div>
  <div class="funded"><div class="f">Funded $0</div><div class="g">Goal $1,000</div></div>
</article>

<article class="abs card" style="left:719px">
  <span class="vline"></span>
  <h3>The elephant with no trunk</h3>
  <div class="pic" role="img" aria-label="Photo of elephants silhouetted at sunset" style="background:linear-gradient(#c98a2a,#e8b14a 45%,#3a2410 80%)"></div>
  <p><b>Ut placerat nunc suscipit metus lacinia vel interdum tortor</b> eleifend. Aliquam erat volutpat. Ut consectetur auctor ornare.</p>
  <div class="backers"><svg width="28" height="28" viewBox="0 0 28 28"><circle cx="9" cy="8" r="4" fill="#b98a5a"/><circle cx="19" cy="8" r="4" fill="#b98a5a"/><path d="M2 22c0-6 14-6 14 0z" fill="#4a7a2a"/><path d="M12 22c0-6 14-6 14 0z" fill="#3a5a8a"/><circle cx="14" cy="14" r="4" fill="#c99a6a"/><path d="M6 28c0-7 16-7 16 0z" fill="#555"/></svg>0</div>
  <div class="funded"><div class="f">Funded $0</div><div class="g">Goal $1,000</div></div>
</article>

<footer class="abs footer"></footer>
<div class="abs foot-brand"><span class="dot"></span><span class="name">VELMORAHUB</span></div>
<span class="abs fsep" style="left:360px"></span>
<span class="abs fsep" style="left:695px"></span>
<div class="abs foot-links">Home &nbsp;~&nbsp; Product List &nbsp;~&nbsp; Delivery Area &nbsp;~&nbsp; Contact Us</div>
<div class="abs follow">Follow Us On:</div>
<div class="abs social"><span></span><span></span><span></span><span></span></div>
<div class="abs copy">VELMORAHUB, Copyright &nbsp;&nbsp; 2012-13, Privacy Policy</div>
<address class="abs contact" style="font-style:normal">
  <h4>Contact Info</h4>
  <b>Velmora Hub</b><br>
  27 Weltmore Close<br>
  Dunvale<br>
  Cape Town<br>
  +263748395026<br>
  +447913462058<br>
  E mail enquiries@VelmoraHub.example
</address>

</body>
</html>
```